Brochure Business Marketing Collateral Fun Project!
Tri-Fold Brochure | Envelope | Business Card
Thank you for the recent designs, I have given some of you PM feedback. You all have great ideas.
Thanks again
**I like the graphical use of the "Plans as low as $50"
**I like the Loomparly and Brindle information
**I like royal blue colors
**I like highlighting the "Key Features" information
Thank you everyone, they look very nice
#11 can you add the Loomparly and Brindle info?
Can you remove the words "toll free" also?
Can you change the "hand picture?"
Thank you
I have been asked to upload the logo in .AI or .EPS format. I have uploaded the new files extensions with multiple color versions to review as well.
Hope this helps, Thank you
Good Morning everyone-We have added some prize money to the project. We want to get this project completed BEFORE the due date.
We are still open to some more ideas.
Thank you to everyone participating!!
Glen
@inkvarda Thank you for the post. You have included all requested info from our brief. We appreciate you paying attention to our request.
#1 & #2 We like your design idea, but need all included content from the uploaded files from the brief. For example, the QR Code, the social icons etc...
Thanks again for the work!
@muvostelle Thank you very nice way to start the project. Can you add the second page information as well to the brochure? It should be submitted. Please let me know if you are unable to see it.
Thanks again Glen
@muvostelle Thank you for the design, looks clean. Can you work on the brochure please?

```html
<!DOCTYPE html>
<html lang="en">
<head>
<meta charset="utf-8">
<title>Multi-Channel Mobile Marketing Brochure</title>
<link href="https://fonts.googleapis.com/css2?family=Open+Sans:wght@300;400;600;700;800&display=swap" rel="stylesheet">
<style>
  :root{
    --royal:#1565c0;
    --heading:#1a73c9;
    --navy:#0b2a6b;
    --deep:#0a3a8c;
    --ink:#3a3f47;
    --dark:#1d2530;
    --paper:#ffffff;
    --mist:#eef2f6;
  }
  *{margin:0;padding:0;box-sizing:border-box}
  html,body{width:1200px;height:926px;overflow:hidden;background:var(--paper)}
  body{font-family:"Open Sans",Arial,sans-serif;color:var(--ink)}
  .brochure{position:relative;width:1200px;height:926px;background:linear-gradient(180deg,#fff 0%,#fff 55%,var(--mist) 78%)}
  .panel{position:absolute;top:0}
  .panel-left{left:30px;width:340px}
  .panel-middle{left:412px;width:375px}
  .panel-right{left:805px;width:385px}
  h2{color:var(--heading);font-weight:700;line-height:1.15}
  .panel-left h2{font-size:22px;color:var(--royal);margin-top:28px;color:var(--paper);background:none}
  .panel-left .lead-title{font-size:22px;color:var(--paper)}
  .left-head{position:absolute;left:0;top:0;width:390px;height:0}
  .title-left{font-size:21px;font-weight:700;color:var(--royal);line-height:1.2;margin-top:26px}
  p{font-size:15px;line-height:1.45}
  .panel-left p{margin-top:12px}
  .stat{margin-top:22px;font-size:21px;line-height:1.25;color:var(--royal);font-weight:400}
  .stat strong{font-size:30px;font-weight:800}
  .envelope-art{position:absolute;left:48px;top:300px;width:330px;height:440px;border-radius:14px;
    background:radial-gradient(circle at 50% 45%,#ffffff 0%,#e3eaf3 55%,#b9cbe2 100%)}
  .panel-middle h2{font-size:26px;margin-top:34px}
  .panel-middle h2.second{margin-top:34px}
  ul{list-style:none;margin-top:10px}
  li{font-size:15px;line-height:1.4;padding-left:14px;position:relative;margin-bottom:8px}
  li::before{content:"•";position:absolute;left:0;color:var(--ink)}
  .panel-middle p{margin-top:12px}
  .plans-title{margin-top:34px;font-size:21px;font-weight:700;color:var(--dark)}
  .plan-box{margin-top:12px;height:74px;border:3px solid #7fb3e6;border-radius:10px;background:var(--paper);
    display:flex;align-items:center;gap:12px;padding:0 14px;font-size:14px;font-weight:700;color:var(--dark);line-height:1.15}
  .plan-box .plus{font-size:24px;color:var(--royal)}
  .plan-box .chip{width:26px;height:26px;border-radius:6px;background:linear-gradient(#5aa2e8,#1f63b8)}
  .panel-right h2{font-size:26px;margin-top:34px}
  .panel-right p{margin-top:12px}
  .channels{margin-top:26px;font-size:17px;line-height:1.5;color:var(--royal)}
  .social-art{position:absolute;left:975px;top:405px;width:200px;height:150px;border-radius:50%;
    background:radial-gradient(circle,#dbe9f7 0%,rgba(219,233,247,0) 70%);display:flex;flex-direction:column;align-items:center;justify-content:center;gap:6px}
  .social-name{font-size:15px;font-weight:700;color:var(--royal);display:flex;align-items:center;gap:6px}
  .social-name i{display:inline-block;width:12px;height:12px;border-radius:50%;background:var(--royal)}
  .portrait{position:absolute;left:800px;top:490px;width:400px;height:350px;
    background:linear-gradient(160deg,#e9eef4 0%,#c9a98e 45%,#6a4634 80%,#2d2a2e 100%);border-radius:6px}
  .wave{position:absolute;left:0;top:700px;width:1200px;height:226px}
  .quote{position:absolute;left:26px;top:796px;width:880px;font-size:24px;font-weight:300;color:var(--paper);line-height:1.35}
</style>
</head>
<body>
<main class="brochure">
  <div class="envelope-art" role="img" aria-label="Illustration of an open envelope with a large email at-sign letter"></div>

  <svg class="wave" viewBox="0 0 1200 226" preserveAspectRatio="none" aria-hidden="true">
    <defs>
      <linearGradient id="band" x1="0" y1="0" x2="0" y2="1">
        <stop offset="0" stop-color="#2b7ad6"/>
        <stop offset="0.5" stop-color="#0f4aa6"/>
        <stop offset="1" stop-color="#0b2a6b"/>
      </linearGradient>
    </defs>
    <path d="M0 30 C 200 -10, 420 60, 700 50 S 1050 20, 1200 40 L1200 226 L0 226 Z" fill="url(#band)"/>
    <path d="M0 55 C 260 20, 480 90, 760 75 S 1080 50, 1200 70" fill="none" stroke="#6fb0f0" stroke-width="3" opacity="0.7"/>
    <path d="M0 75 C 300 45, 520 110, 800 95 S 1100 75, 1200 95" fill="none" stroke="#9ccbf5" stroke-width="1.5" opacity="0.5"/>
  </svg>

  <section class="panel panel-left">
    <h2 class="title-left">Top 500s Utilize Mobile Marketing Because it Works</h2>
    <p>You see Mobile Keywords all over TV, radio, magazines, and Top 500 websites. People text your Keyword to 48215 to join your mobile list. You can then send direct response campaigns.</p>
    <p class="stat"><strong>90%</strong> of text messages get opened, and most get responded to within five minutes!</p>
  </section>

  <section class="panel panel-middle">
    <h2>Mobile Coupons</h2>
    <ul>
      <li>Maximize your marketing strategy with the speed, convenience, and positive return from Mobile Coupons</li>
      <li>Create unique promotion codes for each individual SMS Mobile Coupon</li>
      <li>Easily redeem each coupon using Zinnia Mobile's web-based software</li>
      <li>Track redemption rates and revenue earned</li>
    </ul>
    <h2 class="second">Mobile Keyword Marketing</h2>
    <p>Unlike traditional email subscriptions, mobile keyword subscriptions are controlled by the end users. People can subscribe and unsubscribe on an opt-in basis. This level of control and the new emerging mobile culture have brought keyword marketing to impact levels far exceeding direct mail, email marketing, and other traditional marketing channels, resulting in as much as 90% + read rate and 25%+ response rate.</p>
    <div class="plans-title">All Plans come with...</div>
    <div class="plan-box"><span>Bundled Text<br>Credits</span><span class="chip"></span><span class="plus">+</span><span>FREE<br>Keywords</span><span class="chip"></span></div>
    <div class="plan-box"><span>FREE<br>Emails</span><span class="plus">+</span><span>FREE<br>IM</span><span class="plus">+</span><span>Social<br>Message</span><span class="chip"></span></div>
  </section>

  <section class="panel panel-right">
    <h2>Get the Latest in Multi-Channel Communications</h2>
    <p>Increase response rates, brand awareness, and return on investment using a single webbased software that integrates every popular messaging channel. For the same price others charge for just email or mobile alone, you can upgrade to a service that integrates it ALL.</p>
    <div class="channels">QR Codes<br>Email Marketing<br>Voice Broadcasting<br>Mobile Text Marketing<br>Instant Message Marketing<br>Social Networking (Loomparly, Brindle)</div>
  </section>

  <div class="portrait" role="img" aria-label="Photo of a smiling woman holding a phone in front of sale tags"></div>
  <div class="social-art">
    <span class="social-name"><i></i>Loomparly</span>
    <span class="social-name"><i></i>Brindle</span>
  </div>

  <blockquote class="quote">“Email Marketing is one of the 3 cornerstones of a<br>multi-channel marketing strategy”</blockquote>
</main>
</body>
</html>
```